Sex trafficking Survivor Newsletter

I would like an email newsletter template- mail chimp ready. The first will be a letter to update supporters on all the new changes. see attached.
Another template will have more blocks- for monthly use. I am envisioning a beautiful banner- possibly incorporating logo and photo(black woman holding sun); a main section (cover story, success story, teaching moments); news section; possibly three boxes at the bottom (spotlight- encouraging story of advocate or survivor, Get involved, Events)
I will be using mailchimp.
Let me know if you need more details.

```html
<!DOCTYPE html>
<html lang="en">
<head>
<meta charset="utf-8">
<title>Rise Anew – Partner Update</title>
<link href="https://fonts.googleapis.com/css2?family=Arimo:wght@400;700&family=Playfair+Display:wght@400&display=swap" rel="stylesheet">
<style>
  :root{
    --blue:#0d57a0;
    --heading-blue:#1a5d9e;
    --gold:#f5c518;
    --gold-line:#e8b21a;
    --silver:#c9ccd1;
    --ink:#333333;
    --muted:#555555;
    --link:#1a3fd6;
    --white:#ffffff;
  }
  *{margin:0;padding:0;box-sizing:border-box;}
  html,body{width:845px;height:1200px;overflow:hidden;background:var(--white);}
  body{font-family:"Arimo",Arial,sans-serif;color:var(--ink);}
  .sheet{position:relative;width:845px;height:1200px;overflow:hidden;background:var(--white);}

  .hero-photo{position:absolute;left:0;top:0;width:845px;height:400px;
    background:linear-gradient(90deg,#f6f2ee 0%,#ece3da 28%,#cdb29a 52%,#a77a58 72%,#6e4a34 100%);}
  .shapes{position:absolute;left:0;top:0;}

  .ribbon{position:absolute;left:0;top:22px;}
  .ribbon-text{position:absolute;left:34px;font-size:17px;letter-spacing:.3px;white-space:nowrap;}
  .ribbon-text.one{top:33px;color:var(--blue);}
  .ribbon-text.two{top:61px;color:var(--gold);}
  .ribbon-text.three{top:89px;color:var(--blue);font-weight:700;}

  .brand{position:absolute;text-align:center;white-space:nowrap;}
  .brand-old{left:25px;top:160px;width:170px;}
  .brand-new{left:236px;top:140px;width:270px;}
  .brand-name{font-family:"Playfair Display",Georgia,serif;color:var(--ink);}
  .brand-old .brand-name{font-size:24px;}
  .brand-new .brand-name{font-size:28px;letter-spacing:1px;display:inline-flex;align-items:center;gap:10px;}
  .brand-dot{width:14px;height:14px;border-radius:50%;background:var(--blue);display:inline-block;}
  .brand-label{position:absolute;top:216px;font-size:13px;letter-spacing:2px;color:var(--muted);}
  .label-before{left:77px;}
  .label-now{left:381px;}
  .divider{position:absolute;left:200px;top:137px;height:96px;border-left:3px dotted #b8b8b8;}

  .vision{position:absolute;left:0;top:380px;width:238px;padding:28px 26px 0 25px;color:var(--white);}
  .vision-kicker{color:var(--gold);font-size:24px;font-weight:700;margin-top:2px;}
  .vision-title{font-size:29px;line-height:32.5px;font-weight:700;margin-top:6px;}
  .vision-body{font-size:14px;line-height:19.5px;margin-top:16px;}
  .vision-rule{position:absolute;left:0;top:1103px;width:238px;border-top:1px dashed rgba(255,255,255,.7);}
  .contact{position:absolute;left:33px;top:1124px;list-style:none;color:var(--white);font-size:15px;}
  .contact li{display:flex;align-items:center;gap:8px;height:24px;white-space:nowrap;}
  .contact svg{flex:none;}
  .contact .gold{color:var(--gold);}

  .letter{position:absolute;left:276px;top:428px;width:534px;font-size:14px;line-height:19.6px;color:var(--ink);}
  .salutation{font-size:18px;color:var(--heading-blue);margin-bottom:15px;}
  .letter p{margin-bottom:6px;}
  .letter h2{font-size:21px;color:var(--heading-blue);font-weight:700;margin:24px 0 12px;}
  .letter a{color:var(--link);text-decoration:underline;}
  .signature{position:absolute;left:276px;top:1140px;font-size:14px;color:var(--ink);}
  .site{position:absolute;right:36px;top:1150px;font-size:12.5px;letter-spacing:3.2px;color:var(--muted);
    border-bottom:1px solid #cfcfcf;padding-bottom:3px;white-space:nowrap;}
</style>
</head>
<body>
<div class="sheet">

  <div class="hero-photo" role="img" aria-label="Photograph of a smiling young woman with a red headband in front of a brick city building, bathed in warm sunlight"></div>

  <svg class="shapes" width="845" height="1200" viewBox="0 0 845 1200" aria-hidden="true">
    <path d="M0,252 C80,262 190,300 240,384 L240,1200 L0,1200 Z" fill="var(--blue)"/>
    <path d="M0,252 C80,262 190,300 240,384" fill="none" stroke="var(--gold-line)" stroke-width="4"/>
    <path d="M240,1200 L240,384 C300,340 420,372 560,392 C680,408 780,380 845,322 L845,1200 Z" fill="var(--white)"/>
    <path d="M240,384 C300,340 420,372 560,392 C680,408 780,380 845,322" fill="none" stroke="var(--silver)" stroke-width="6"/>
    <path d="M236,388 C300,348 420,380 560,400 C680,416 780,388 845,332" fill="none" stroke="var(--gold-line)" stroke-width="2.5"/>
  </svg>

  <svg class="ribbon" width="210" height="100" viewBox="0 0 210 100" aria-hidden="true">
    <polygon points="0,0 112,0 128,15 112,30 0,30" fill="var(--gold)"/>
    <polygon points="0,30 160,30 180,48 160,66 0,66" fill="var(--blue)"/>
    <polygon points="0,66 182,66 200,83 182,100 0,100" fill="var(--gold)"/>
  </svg>
  <div class="ribbon-text one">WE’VE</div>
  <div class="ribbon-text two">MADE SOME</div>
  <div class="ribbon-text three">CHANGES...</div>

  <div class="brand brand-old"><span class="brand-name">Willow Creek</span></div>
  <div class="divider"></div>
  <div class="brand brand-new"><span class="brand-name"><span class="brand-dot"></span>Rise Anew</span></div>
  <div class="brand-label label-before">BEFORE</div>
  <div class="brand-label label-now">NOW</div>

  <aside class="vision">
    <div class="vision-kicker">Our Vision</div>
    <h1 class="vision-title">Survivors of sexual exploitation live free, fulfilling their God-given purpose.</h1>
    <p class="vision-body">In order to see our Vision become a reality, we need your help. While continuing to serve ladies with a street outreach initiative and educational classes, we are launching a mentorship program for female mentors to be paired with women who desperately need an advocate. Many survivors have never experienced a healthy supportive relationship, and do not know their God-given purpose. Your financial support will help us to continue to serve ladies in the community and launch this new life-changing initiative.</p>
  </aside>
  <div class="vision-rule"></div>
  <ul class="contact">
    <li>
      <svg width="16" height="12" viewBox="0 0 16 12"><rect x="0.5" y="0.5" width="15" height="11" fill="var(--gold)"/><path d="M1,1 L8,7 L15,1" fill="none" stroke="var(--blue)" stroke-width="1.4"/></svg>
      <span>lena@<span class="gold">riseanew</span>.org</span>
    </li>
    <li>
      <svg width="14" height="14" viewBox="0 0 14 14"><circle cx="7" cy="7" r="6" fill="none" stroke="var(--gold)" stroke-width="1.4"/><ellipse cx="7" cy="7" rx="2.6" ry="6" fill="none" stroke="var(--gold)" stroke-width="1.2"/><line x1="1" y1="7" x2="13" y2="7" stroke="var(--gold)" stroke-width="1.2"/></svg>
      <span>www.<span class="gold">riseanew</span>.org</span>
    </li>
  </ul>

  <main class="letter">
    <div class="salutation">Dear Partner in Ministry</div>
    <p>I am writing to tell you of some exciting updates with Willow Creek. We have seen amazing transformation in the lives of sexually exploited women since 2011, and we couldn’t have done this without your support and partnership. Women have literally started new lives and escaped the horrors of their past abuse.</p>

    <h2>NEW Name</h2>
    <p>We officially changed our name to “Rise Anew” to emphasize the total transformation women experience and the freedom this brings. To be truly free and alive, a woman will experience change physically, emotionally, intellectually, and spiritually. Our name change highlights what women experience as we walk beside them. Many women say they were “just existing” in their former life. Now, they feel alive – many for the first time.</p>

    <h2>NEW Executive Director:</h2>
    <p>While God has allowed me to be a part of such incredible transformation, I felt it was time to step down and bring on a new Executive Director to carry forward the vision and to take the organization to the next level. You have been incredibly supportive and compassionate during my health challenges. My family and I cannot thank you enough for your prayers and love.</p>
    <p>I am pleased to announce the board and I have selected Lena Marsh (lena@riseanew.org), who comes to us with over 15 years of non-profit management experience. She has successfully developed initiatives that engaged thousands of people in ministry to the poor. We are thrilled to have her leading the effort to accomplish the mission to “mobilize communities to encourage and equip survivors of sexual exploitation to build new lives.”</p>
    <p>It is a blessing that I can step away knowing we are in good hands and that God will continue to work through this ministry for His glory. I pray you will consider financially committing to the ministry and being a mentor so that we can continue to empower the survivors of sexual exploitation here in Dallas. Please visit us at <a href="#">www.riseanew.org</a></p>
    <p>With love and appreciation,</p>
  </main>

  <div class="signature">Dana Whitfield</div>
  <div class="site">www.riseanew.org</div>
</div>
</body>
</html>
```